Investment company seeks website design

TBW (Tallowbrook Wealth Partners) are an investment company that actively targets and acquires businesses and grows them after acquisition.

The website design needs to be professional and should communicate to key decision-makers inside the acquirable companies that TBW targets.

You will design the Homepage initially for the competition. If you win the competition, you will design the inner pages too.

More details are attached below.

Target Market(s)

Business owners and decision makers inside acquirable companies

Industry/Entity Type

Company Investment

Number of Pages Required

5+ page

Requirements
Must have
• High Attention to Detail. Following the Wireframes closely. Consistent colour and design choices
Should not have
• Anything cheap, too bright or untidy

```html
<!DOCTYPE html>
<html lang="en">
<head>
<meta charset="utf-8">
<title>Tallowbrook Wealth Partners</title>
<link href="https://fonts.googleapis.com/css2?family=Poppins:wght@300;400;500;600;700&display=swap" rel="stylesheet">
<style>
:root{
  --bg:#07142b;
  --bg-deep:#050f22;
  --card:#0e2346;
  --card-line:#2a4a7c;
  --green:#7cc142;
  --green-dark:#5ea12c;
  --white:#ffffff;
  --muted:#b9c4d8;
  --gold:#e0b640;
}
*{box-sizing:border-box;margin:0;padding:0}
html,body{width:1200px;height:4180px;overflow:hidden}
body{background:var(--bg);color:var(--white);font-family:'Poppins',sans-serif;position:relative}
.abs{position:absolute}
.btn{display:inline-block;background:var(--green);color:var(--white);font-size:13px;font-weight:500;border-radius:20px;padding:10px 30px}
p.body{font-size:13px;line-height:1.6;color:var(--muted)}
h2.section-title{font-size:40px;font-weight:500;line-height:1.2;text-transform:uppercase}

/* nav */
.site-nav{top:0;left:0;width:1200px;height:100px}
.brand{left:110px;top:26px;display:flex;align-items:center;gap:12px}
.brand-mark{width:36px;height:36px;background:var(--green);border-radius:4px}
.brand-name{font-size:17px;font-weight:600;line-height:1.1;text-transform:uppercase;letter-spacing:1px}
.nav-links{left:370px;top:44px;display:flex;gap:40px;font-size:13px}
.nav-links .active{color:var(--green)}
.nav-login{left:960px;top:32px;padding:9px 34px}

/* hero */
.hero-art{left:600px;top:30px;width:560px;height:540px;border-radius:40% 20% 30% 40%;
  background:radial-gradient(circle at 55% 65%,#b8902a 0%,#5b4a1a 25%,#173a2f 50%,rgba(7,20,43,0) 72%)}
.hero-title{left:110px;top:180px;font-size:52px;font-weight:500;line-height:1.15;text-transform:uppercase;width:560px}
.hero-text{left:110px;top:390px;width:470px}
.hero-btn{left:110px;top:462px}

/* stats */
.stats{left:112px;top:700px;width:976px;display:flex;gap:32px}
.stat{width:220px;height:120px;background:var(--card);border:1px solid var(--card-line);border-radius:6px;text-align:center;padding-top:26px}
.stat-value{font-size:38px;font-weight:600;line-height:1.1}
.stat-label{font-size:13px;color:var(--muted);margin-top:8px}

/* welcome */
.welcome-photo{left:110px;top:920px;width:460px;height:470px;clip-path:polygon(50% 0,100% 25%,100% 75%,50% 100%,0 75%,0 25%);
  background:linear-gradient(135deg,#6f7d93,#2d3b55 60%,#142240)}
.welcome-chip{left:60px;top:1290px;width:190px;height:100px;background:#13305e;border:2px solid #3a65a8;border-radius:6px}
.welcome-chip svg{display:block;margin:18px auto}
.welcome-title{left:640px;top:1010px;width:520px;font-size:36px;font-weight:500;line-height:1.2;text-transform:uppercase}
.welcome-text{left:640px;top:1110px;width:500px}
.feature-list{left:640px;top:1210px;width:470px;display:grid;grid-template-columns:1fr 1fr;row-gap:12px;font-size:13px;list-style:none}
.feature-list li{display:flex;align-items:center;gap:10px}
.feature-list li::before{content:"";width:12px;height:12px;border-radius:50%;border:2px solid var(--muted)}
.welcome-btn{left:640px;top:1320px}

/* video */
.video{left:112px;top:1520px;width:976px;height:450px;border-radius:6px;background:linear-gradient(120deg,#5a4637,#8b7a6c 35%,#c7c9cf 60%,#394a66)}
.play{left:555px;top:1700px;width:90px;height:90px;border-radius:50%;background:var(--green);display:flex;align-items:center;justify-content:center}

/* plans */
.plans-title{left:0;top:2030px;width:1200px;text-align:center}
.plans-text{left:300px;top:2150px;width:600px;text-align:center}
.plans{left:112px;top:2225px;display:flex;gap:24px}
.plan{width:226px;height:340px;background:var(--card);border:1px solid var(--card-line);border-radius:8px;padding:26px 22px}
.plan-name{font-size:15px;padding-bottom:14px;border-bottom:1px solid var(--card-line)}
.plan-price{font-size:42px;font-weight:600;margin:22px 0 18px}
.plan-meta{font-size:14px;line-height:2;color:var(--white)}
.plan .btn{margin:36px 0 0 28px}
.arrow{top:2385px}

/* long term */
.long-title{left:120px;top:2820px;width:460px;font-size:40px;font-weight:500;line-height:1.2;text-transform:uppercase}
.long-text{left:120px;top:2940px;width:440px}
.long-btn{left:120px;top:3090px}
.long-photo{left:610px;top:2750px;width:470px;height:470px;clip-path:polygon(50% 0,100% 25%,100% 75%,50% 100%,0 75%,0 25%);
  background:linear-gradient(150deg,#e8ecf2 0%,#9aa3b2 40%,#3a3a46 75%,#1c2436)}
.long-chart{left:890px;top:3030px;width:200px;height:150px;background:#102a55;border:2px solid #3a65a8;border-radius:6px;padding:10px}
.long-chart .cap{font-size:9px;color:var(--muted);margin-bottom:8px}
.long-badge{left:580px;top:2920px;width:44px;height:44px;background:#13305e;border:2px solid #3a65a8;border-radius:4px}

/* testimonials */
.reviews-title{left:0;top:3320px;width:1200px;text-align:center;font-size:36px}
.reviews{left:112px;top:3410px;display:flex;gap:40px}
.review{width:214px}
.stars{display:flex;gap:4px;margin-bottom:16px}
.review p{font-size:12px;line-height:1.6;color:var(--muted)}
.reviewer{display:flex;align-items:center;gap:10px;margin-top:22px;font-size:12px}
.avatar{width:40px;height:40px;border-radius:50%;background:#3a4e70}
.reviewer small{display:block;color:var(--muted);font-size:11px}

/* newsletter */
.newsletter{left:120px;top:3750px;width:960px;height:190px;border-radius:10px;background:linear-gradient(135deg,var(--green),#5e9f2e)}
.newsletter h2{position:absolute;left:0;top:34px;width:960px;text-align:center;font-size:36px;font-weight:500;text-transform:uppercase}
.signup{position:absolute;left:180px;top:112px;width:600px;height:44px;background:var(--white);border-radius:22px;display:flex;align-items:center;justify-content:space-between;padding-left:22px}
.signup span{font-size:12px;color:#7a8394}
.signup .submit{background:#1f3f7a;color:var(--white);font-size:13px;border-radius:22px;padding:12px 40px}

/* footer */
.footer-brand{left:120px;top:3980px}
.footer-about{left:120px;top:4036px;width:240px;font-size:11px;line-height:1.5;color:var(--muted)}
.footer-col{top:3978px}
.footer-col h3{font-size:17px;font-weight:500;margin-bottom:8px;line-height:1.4}
.footer-col li{list-style:none;font-size:12px;color:var(--muted);line-height:1.6;display:flex;align-items:center;gap:8px;margin-bottom:2px}
.dot{width:14px;height:14px;border-radius:50%;background:var(--green);flex:none}
.copyright{left:0;top:4148px;width:1200px;height:32px;border-top:1px solid #1c2f52;text-align:center;font-size:11px;color:var(--muted);padding-top:8px}
</style>
</head>
<body>

<header class="abs site-nav">
  <div class="abs brand"><span class="brand-mark"></span><span class="brand-name">Tallowbrook<br>Wealth Partners</span></div>
  <nav class="abs nav-links"><span class="active">Home</span><span>About us</span><span>Our Services</span><span>Our Portfolios</span><span>News</span><span>Contact Us</span></nav>
  <span class="abs btn nav-login">Login</span>
</header>

<div class="abs hero-art" role="img" aria-label="Smartphone with gold coin stacks, glowing growth chart lines and a world map"></div>
<h1 class="abs hero-title">Catch Smart Investments For The Future</h1>
<p class="abs body hero-text">Lorem Ipsum is simply dummy text of the printing and typesetting industry. Lorem Ipsum has been the industry's standard dummy text ever since the 1500s.</p>
<span class="abs btn hero-btn">Invest now</span>

<section class="abs stats">
  <div class="stat"><div class="stat-value">$198M+</div><div class="stat-label">Total funds disbursed</div></div>
  <div class="stat"><div class="stat-value">18%</div><div class="stat-label">Return average</div></div>
  <div class="stat"><div class="stat-value">98K+</div><div class="stat-label">Registered investors</div></div>
  <div class="stat"><div class="stat-value">$198K+</div><div class="stat-label">2021 Loan accumulation</div></div>
</section>

<div class="abs welcome-photo" role="img" aria-label="Two colleagues working together at a laptop in an office"></div>
<div class="abs welcome-chip">
  <svg width="150" height="60" viewBox="0 0 150 60"><polyline points="0,50 20,30 38,40 58,14 78,34 100,20 120,36 150,8" fill="none" stroke="#7cc142" stroke-width="3"/><g fill="#5a86c8"><rect x="10" y="46" width="8" height="14"/><rect x="40" y="42" width="8" height="18"/><rect x="70" y="38" width="8" height="22"/><rect x="100" y="44" width="8" height="16"/><rect x="130" y="36" width="8" height="24"/></g></svg>
</div>
<h2 class="abs welcome-title">Welcome to Tallowbrook Wealth Partners</h2>
<p class="abs body welcome-text">Lorem Ipsum is simply dummy text of the printing and typesetting industry. Lorem Ipsum has been the industry's standard dummy text ever since the 1500s.</p>
<ul class="abs feature-list">
  <li>Smart Capital</li><li>Easy Transaction Access</li>
  <li>Attractive returns</li><li>Social Impact</li>
  <li>Security</li>
</ul>
<span class="abs btn welcome-btn">Invest now</span>

<div class="abs video" role="img" aria-label="Business team meeting around a table with charts and tablets"></div>
<div class="abs play"><svg width="34" height="34" viewBox="0 0 34 34"><path d="M10 6 L28 17 L10 28 Z" fill="#fff"/></svg></div>

<h2 class="abs section-title plans-title">Choose The Investment For<br>Your Plan</h2>
<p class="abs body plans-text">Lorem Ipsum is simply dummy text of the printing and typesetting industry. Lorem Ipsum has been the industry's standard dummy text ever since the 1500s, when an unknown printer took a galley of type.</p>
<svg class="abs arrow" style="left:58px" width="20" height="30" viewBox="0 0 20 30"><path d="M15 4 L5 15 L15 26" fill="none" stroke="#b9c4d8" stroke-width="3"/></svg>
<svg class="abs arrow" style="left:1122px" width="20" height="30" viewBox="0 0 20 30"><path d="M5 4 L15 15 L5 26" fill="none" stroke="#b9c4d8" stroke-width="3"/></svg>
<section class="abs plans">
  <div class="plan"><div class="plan-name">Gold</div><div class="plan-price">$6,888</div><div class="plan-meta">Margin : 25%/ Year<br>Duration : 7 months</div><span class="btn">Invest now</span></div>
  <div class="plan"><div class="plan-name">Mutual Funds</div><div class="plan-price">$6,688</div><div class="plan-meta">Margin : 25%/ Year<br>Duration : 7 months</div><span class="btn">Invest now</span></div>
  <div class="plan"><div class="plan-name">Deposit</div><div class="plan-price">$5,880</div><div class="plan-meta">Margin : 25%/ Year<br>Duration : 7 months</div><span class="btn">Invest now</span></div>
  <div class="plan"><div class="plan-name">Investment in stocks</div><div class="plan-price">$1,898</div><div class="plan-meta">Margin : 25%/ Year<br>Duration : 7 months</div><span class="btn">Invest now</span></div>
</section>

<h2 class="abs long-title">Invest Money For<br>The Long Term</h2>
<p class="abs body long-text">Lorem Ipsum is simply dummy text of the printing and typesetting industry. Lorem Ipsum has been the industry's standard dummy text ever since the 1500s, when an unknown printer took a galley of type and scrambled it to make a type specimen book. It has survived not only five centuries, but also the leap into electronic.</p>
<span class="abs btn long-btn">Invest now</span>
<div class="abs long-photo" role="img" aria-label="Smiling businessman using a smartphone in front of office buildings"></div>
<div class="abs long-badge"></div>
<div class="abs long-chart">
  <div class="cap">Long Term Investment Graph</div>
  <svg width="176" height="100" viewBox="0 0 176 100"><g fill="#5a86c8"><rect x="6" y="60" width="18" height="40"/><rect x="34" y="44" width="18" height="56"/><rect x="62" y="52" width="18" height="48"/><rect x="90" y="30" width="18" height="70"/><rect x="118" y="38" width="18" height="62"/><rect x="146" y="16" width="18" height="84"/></g><polyline points="15,50 43,34 71,42 99,20 127,28 155,6" fill="none" stroke="#7cc142" stroke-width="2"/></svg>
</div>

<h2 class="abs section-title reviews-title">What Our Customers Have To Say</h2>
<section class="abs reviews">
  <div class="review">
    <div class="stars"><svg width="110" height="18" viewBox="0 0 110 18"><g fill="#e0b640"><path id="s" d="M9 0l2.6 5.6 6 .6-4.5 4 1.3 6L9 13.2 3.6 16.2l1.3-6L.4 6.2l6-.6z"/><use href="#s" x="22"/><use href="#s" x="44"/><use href="#s" x="66"/><use href="#s" x="88"/></g></svg></div>
    <p>Lorem Ipsum is simply dummy text of the printing and typesetting industry. Lorem Ipsum has been the industry's standard dummy text ever since the</p>
    <div class="reviewer"><span class="avatar"></span><span>Nora Ellison<small>Business owner</small></span></div>
  </div>
  <div class="review">
    <div class="stars"><svg width="110" height="18" viewBox="0 0 110 18"><g fill="#e0b640"><use href="#s"/><use href="#s" x="22"/><use href="#s" x="44"/><use href="#s" x="66"/><use href="#s" x="88"/></g></svg></div>
    <p>Lorem Ipsum is simply dummy text of the printing and typesetting industry. Lorem Ipsum has been the industry's standard dummy text ever since the</p>
    <div class="reviewer"><span class="avatar"></span><span>Owen Hartley<small>Company director</small></span></div>
  </div>
  <div class="review">
    <div class="stars"><svg width="110" height="18" viewBox="0 0 110 18"><g fill="#e0b640"><use href="#s"/><use href="#s" x="22"/><use href="#s" x="44"/><use href="#s" x="66"/><use href="#s" x="88"/></g></svg></div>
    <p>Lorem Ipsum is simply dummy text of the printing and typesetting industry. Lorem Ipsum has been the industry's standard dummy text ever since the</p>
    <div class="reviewer"><span class="avatar"></span><span>Mara Quinlan<small>Founder</small></span></div>
  </div>
  <div class="review">
    <div class="stars"><svg width="110" height="18" viewBox="0 0 110 18"><g fill="#e0b640"><use href="#s"/><use href="#s" x="22"/><use href="#s" x="44"/><use href="#s" x="66"/><use href="#s" x="88"/></g></svg></div>
    <p>Lorem Ipsum is simply dummy text of the printing and typesetting industry. Lorem Ipsum has been the industry's standard dummy text ever since the</p>
    <div class="reviewer"><span class="avatar"></span><span>Felix Dorran<small>Managing partner</small></span></div>
  </div>
</section>

<section class="abs newsletter">
  <h2>Subscribe Your Newsletter</h2>
  <div class="signup"><span>Enter Your Email ID</span><span class="submit">Subscribe</span></div>
</section>

<footer>
  <div class="abs brand footer-brand"><span class="brand-mark"></span><span class="brand-name">Tallowbrook<br>Wealth Partners</span></div>
  <p class="abs footer-about">Lorem Ipsum is simply dummy text of the printing and typesetting industry. Lorem Ipsum has been the industry's standard dummy text ever since the 1500s, when an unknown printer took a galley of type and scrambled it.</p>
  <div class="abs footer-col" style="left:430px"><h3>Menu</h3><ul><li>Home</li><li>About us</li><li>Our Services</li><li>Our Portfolios</li><li>News</li><li>Contact Us</li></ul></div>
  <div class="abs footer-col" style="left:610px"><h3>Contact Us</h3><ul><li><span class="dot"></span>(02) 555 0148</li><li><span class="dot"></span>12 Harbour Lane, Suite 4</li><li><span class="dot"></span>hello@tallowbrookwealth.com</li></ul></div>
  <div class="abs footer-col" style="left:920px"><h3>Follow us</h3><ul><li><span class="dot"></span>Newsfeed</li><li><span class="dot"></span>Photostream</li><li><span class="dot"></span>Video Channel</li><li><span class="dot"></span>Microblog</li></ul></div>
  <div class="abs copyright">Copyright © 2014-2024 Tallowbrook Wealth Partners - All right reserved</div>
</footer>

</body>
</html>
```